We need a poster design for "KEVO Sports Night" events. The events have been around for 3 years and we hope the poster will give a sense of vibrant and active designs. It is more to a community event with teamwork and fun.

I have uploaded a past event poster just FYI.

Target Market(s)

Community, Family

Industry/Entity Type

Non Profit

Logo Text

KEVO Sports Night

Requirements
Must have
• KEVO Sports Night
• Organiser: KEVO Sydney
• Date: 25/11/2017
• Time: 4:00pm
• Venue: Wendamere Park
• Facebook: kevosport

```html
<!DOCTYPE html>
<html lang="en">
<head>
<meta charset="utf-8">
<title>KEVO Sports Night</title>
<link href="https://fonts.googleapis.com/css2?family=Arimo:wght@700&family=Open+Sans:wght@700&display=swap" rel="stylesheet">
<style>
  :root {
    --orange: #ee5a12;
    --orange-fade: rgba(238, 90, 18, 0);
    --paper-top: #f7f7f7;
    --paper-bottom: #d9d9d9;
    --brown: #3a130c;
    --red: #e3150f;
    --teal: #1f96ae;
    --black: #111111;
    --white: #ffffff;
    --yellow: #f5d41c;
    --gold: #e6b955;
    --ink: #151515;
    --fb-blue: #3a5a98;
  }
  * { margin: 0; padding: 0; box-sizing: border-box; }
  html, body { width: 960px; height: 1200px; overflow: hidden; background: #ffffff; }
  .poster {
    position: relative;
    width: 960px;
    height: 1200px;
    background: linear-gradient(180deg, var(--orange) 0%, #d8672b 40%, #d9b9a8 62%, #cfcfcf 75%, #c9c9c9 100%);
    font-family: "Arimo", Arial, sans-serif;
  }
  .sheet {
    position: absolute;
    left: 20px; right: 18px; top: 22px; bottom: 0;
    background: linear-gradient(180deg, var(--paper-top) 0%, #f2f2f2 60%, var(--paper-bottom) 100%);
  }
  .sheet-rule {
    position: absolute;
    left: 18px; right: 16px; bottom: 18px;
    height: 2px;
    background: var(--gold);
  }
  .sheet-rule-side {
    position: absolute;
    bottom: 18px;
    width: 2px; height: 120px;
    background: linear-gradient(0deg, var(--gold), rgba(230,185,85,0));
  }
  .title { position: absolute; left: 0; width: 100%; text-align: center; font-weight: 700; }
  .title-org { top: 58px; font-size: 104px; line-height: 1; color: var(--brown); letter-spacing: 1px; }
  .title-event { top: 164px; font-size: 98px; line-height: 1; color: var(--red); left: 30px; }
  .runners {
    position: absolute;
    left: 0; top: 300px;
    width: 922px; height: 550px;
    background: linear-gradient(90deg, #f2bb2a 0%, #2fb9c4 22%, #8cc83a 40%, #f0a62f 58%, #3c8fae 74%, #e5261a 92%);
    opacity: 0.85;
    -webkit-mask-image: radial-gradient(ellipse 60% 55% at 55% 50%, #000 60%, transparent 100%);
            mask-image: radial-gradient(ellipse 60% 55% at 55% 50%, #000 60%, transparent 100%);
  }
  .date-badge { position: absolute; left: 268px; top: 428px; width: 380px; height: 210px; }
  .date-text {
    position: absolute; left: 268px; top: 468px; width: 380px;
    text-align: center; font-weight: 700; line-height: 1.05;
  }
  .date-day { font-size: 60px; color: var(--white); letter-spacing: -1px; }
  .date-time { font-size: 50px; color: var(--yellow); }
  .venue {
    position: absolute; top: 920px; left: 0; width: 100%;
    display: flex; justify-content: center; align-items: center; gap: 12px;
    color: var(--teal); font-size: 80px; font-weight: 700; line-height: 1;
  }
  .venue-pin { width: 44px; height: 66px; }
  .footer {
    position: absolute; top: 1084px; left: 0; width: 100%;
    display: flex; justify-content: center; align-items: center; gap: 72px;
    font-family: "Open Sans", Arial, sans-serif; font-weight: 700; font-size: 36px; color: var(--ink);
  }
  .footer-item { display: flex; align-items: center; gap: 14px; }
  .org-mark { width: 80px; height: 80px; border-radius: 50%; border: 2px solid var(--ink); }
  .social-mark { width: 56px; height: 56px; border-radius: 8px; background: var(--fb-blue); }
</style>
</head>
<body>
  <main class="poster">
    <div class="sheet">
      <h1 class="title title-org">KEVO</h1>
      <h2 class="title title-event">Sports Night</h2>

      <div class="runners" role="img" aria-label="Colourful overlapping silhouettes of runners sprinting to the right"></div>

      <svg class="date-badge" viewBox="0 0 380 210" aria-hidden="true">
        <polygon points="6,10 374,0 362,206 40,200" fill="var(--black)"/>
      </svg>
      <div class="date-text">
        <div class="date-day">25-11-2017</div>
        <div class="date-time">4:00pm</div>
      </div>

      <div class="venue">
        <svg class="venue-pin" viewBox="0 0 44 66" aria-hidden="true">
          <path d="M22 2C10.4 2 2 10.6 2 22c0 15 20 42 20 42s20-27 20-42C42 10.6 33.6 2 22 2z" fill="var(--teal)"/>
          <circle cx="22" cy="21" r="8" fill="var(--paper-top)"/>
        </svg>
        <span>Wendamere Park</span>
      </div>

      <div class="footer">
        <div class="footer-item">
          <span class="org-mark" aria-hidden="true"></span>
          <span>KEVO Sydney</span>
        </div>
        <div class="footer-item">
          <span class="social-mark" aria-hidden="true"></span>
          <span>kevosport</span>
        </div>
      </div>

      <div class="sheet-rule"></div>
      <div class="sheet-rule-side" style="left:18px"></div>
      <div class="sheet-rule-side" style="right:16px"></div>
    </div>
  </main>
</body>
</html>
```